Talvick Industrial Maintenance Business Card

Design a business card with the following information, logo must be included.
Talvick Industrial Maintenance
Dan Pelfrey Jr.
Pone 555-214-7608
email dan.pelfrey.jr@mailvantor.com

```html
<!DOCTYPE html>
<html lang="en">
<head>
<meta charset="utf-8">
<title>Talvick Industrial Maintenance – Business Card</title>
<link href="https://fonts.googleapis.com/css2?family=Montserrat:wght@400;600;800&display=swap" rel="stylesheet">
<style>
  :root {
    --backdrop: #272727;
    --card: #ffffff;
    --brand-blue: #0a70b8;
    --charcoal: #212529;
    --band-grey: #c3c3c3;
    --ink: #1b1b1b;
  }
  * { margin: 0; padding: 0; box-sizing: border-box; }
  html, body { width: 1200px; height: 1200px; overflow: hidden; }
  body {
    background: var(--backdrop);
    font-family: "Montserrat", Arial, sans-serif;
    position: relative;
  }
  .card {
    position: absolute;
    left: 180px;
    width: 840px;
    height: 480px;
    background: var(--card);
    overflow: hidden;
    box-shadow: 0 24px 50px rgba(0,0,0,0.55);
  }
  .card--front { top: 90px; }
  .card--back { top: 630px; }
  .card__art { position: absolute; inset: 0; width: 100%; height: 100%; }

  .brand {
    position: absolute;
    display: flex;
    align-items: center;
    color: var(--brand-blue);
    font-weight: 800;
    text-transform: uppercase;
  }
  .brand__dot { border-radius: 50%; background: var(--brand-blue); flex: none; }
  .brand--front { left: 110px; top: 120px; gap: 30px; font-size: 44px; line-height: 1.1; }
  .brand--front .brand__dot { width: 120px; height: 120px; }
  .brand--back { left: 560px; top: 120px; gap: 14px; font-size: 19px; line-height: 1.15; }
  .brand--back .brand__dot { width: 54px; height: 54px; }

  .name-plate {
    position: absolute;
    left: 110px; top: 150px;
    width: 420px; height: 86px;
    display: flex; align-items: center; justify-content: center;
    color: #fff;
    font-weight: 800;
    font-size: 40px;
    letter-spacing: 0.5px;
    text-transform: uppercase;
  }

  .contact-list { position: absolute; left: 70px; top: 262px; list-style: none; }
  .contact-list li {
    display: flex; align-items: center; gap: 22px;
    font-size: 25px; color: var(--ink); height: 50px; margin-bottom: 6px;
    white-space: nowrap;
  }
  .contact-list svg { width: 50px; height: 50px; flex: none; }
</style>
</head>
<body>

<section class="card card--front" aria-label="Card front">
  <svg class="card__art" viewBox="0 0 840 480" preserveAspectRatio="none" aria-hidden="true">
    <polygon fill="var(--charcoal)" points="0,480 840,480 840,350 0,445"/>
    <polygon fill="var(--brand-blue)" points="0,440 840,345 840,350 0,445"/>
    <polygon fill="var(--brand-blue)" points="0,405 215,384 240,410 0,438"/>
    <polygon fill="var(--brand-blue)" points="590,340 840,310 840,346 605,372"/>
  </svg>
  <div class="brand brand--front">
    <span class="brand__dot"></span>
    <span class="brand__name">Talvick<br>Industrial Maintenance</span>
  </div>
</section>

<section class="card card--back" aria-label="Card back">
  <svg class="card__art" viewBox="0 0 840 480" preserveAspectRatio="none" aria-hidden="true">
    <polygon fill="var(--band-grey)" points="0,215 420,110 455,200 0,265"/>
    <polygon fill="var(--brand-blue)" points="95,150 520,130 545,215 120,245"/>
    <polygon fill="var(--charcoal)" points="0,480 840,480 840,345 0,472"/>
    <polygon fill="var(--brand-blue)" points="0,467 840,340 840,345 0,472"/>
    <polygon fill="var(--brand-blue)" points="580,330 840,290 840,342 595,380"/>
  </svg>
  <div class="name-plate">Dan Pelfrey Jr.</div>
  <div class="brand brand--back">
    <span class="brand__dot"></span>
    <span class="brand__name">Talvick<br>Industrial Maintenance</span>
  </div>
  <ul class="contact-list">
    <li>
      <svg viewBox="0 0 56 56" aria-hidden="true">
        <polygon fill="var(--brand-blue)" points="4,10 40,4 54,28 40,52 4,46"/>
        <path fill="#fff" d="M17 20c2-2 4-2 5 0l2 4c1 1 0 2-1 3l-1 1c1 3 4 6 7 7l1-1c1-1 2-2 3-1l4 2c2 1 2 3 0 5-3 3-8 2-13-3s-7-11-7-17z"/>
      </svg>
      <span>555-214-7608</span>
    </li>
    <li>
      <svg viewBox="0 0 56 56" aria-hidden="true">
        <polygon fill="var(--brand-blue)" points="4,10 40,4 54,28 40,52 4,46"/>
        <rect x="13" y="18" width="26" height="19" fill="#fff"/>
        <polyline points="13,18 26,29 39,18" fill="none" stroke="var(--brand-blue)" stroke-width="2.5"/>
      </svg>
      <span>dan.pelfrey.jr@mailvantor.com</span>
    </li>
  </ul>
</section>

</body>
</html>
```